Quiz Company needs two PDF sheets designing

We need two different A4 sheets to be designed - similar to those attached - they need to be at least two-coloured - A4 horizontal layout

The Bingo sheet is as per the attached Word mock up and is similar to the Bingo PDF attached

The Cellraiders sheet should feature 24 hexagons in 6 vertical rows of 4 hexagons

Font styles to use
Serif

Requirements
Must have
• PDF file at least two colours
• www.marlowtrivet.co.uk - 01632 960481 and our logo somewhere on the sheet
Nice to have
• Right Hand Side - Bingo - A Six x Six Grid of round squares with space to write numbers and answers in
• Left Hand side - Space for instructions Numbers 1 to 36 with space for answers - then a mini grid with just circles and space to write numbers in see attached mock up.
• Cellraiders - Right hand side will be 6 lines of 4 hexagons all connecting as per the example - top left numbers 1 to 24 and a small grid for just numbers
• Both sheets also have instructions

```html
<!DOCTYPE html>
<html lang="en">
<head>
<meta charset="utf-8">
<title>Marlow Trivet – Quiz Answer Sheets</title>
<link href="https://fonts.googleapis.com/css2?family=Saira+Condensed:ital,wght@1,800&family=Roboto+Condensed:wght@400;700&display=swap" rel="stylesheet">
<style>
  :root{
    --ink:#3d4599;
    --ink-deep:#2c3390;
    --lavender:#a3a7d8;
    --paper:#ffffff;
    --backdrop:#bdbdbd;
    --body-font:"Roboto Condensed", "Arial Narrow", sans-serif;
    --display-font:"Saira Condensed", "Arial Narrow", sans-serif;
  }
  *{box-sizing:border-box;margin:0;padding:0}
  html,body{width:1200px;height:1200px;overflow:hidden}
  body{background:var(--backdrop);position:relative;font-family:var(--body-font);color:var(--ink)}
  .sheet{position:absolute;background:var(--paper);overflow:hidden}
  .sheet--bingo{left:222px;top:58px;width:736px;height:521px}
  .sheet--cells{left:221px;top:622px;width:742px;height:524px}

  /* Bingo header */
  .bingo-header{position:absolute;left:0;top:17px;width:736px;height:40px;
    background:linear-gradient(90deg,var(--ink) 0,var(--ink) 64%,var(--lavender) 100%)}
  .sheet-title{font-family:var(--display-font);font-style:italic;font-weight:800;letter-spacing:1px;line-height:1}
  .bingo-header .sheet-title{position:absolute;left:42px;top:2px;font-size:38px;color:#fff}
  .contact{font-size:10px;font-weight:700;line-height:16px}
  .bingo-header .contact{position:absolute;left:275px;top:3px;color:#fff}
  .contact .icon{display:inline-block;width:9px;height:9px;vertical-align:-1px;margin-right:4px}
  .brand{font-family:var(--body-font);font-weight:700;font-size:15px;white-space:nowrap}
  .bingo-header .brand{position:absolute;left:540px;top:11px;color:var(--ink-deep)}
  .brand .dot{display:inline-block;width:9px;height:9px;border-radius:50%;background:currentColor;margin-right:6px;vertical-align:0}

  /* Bingo answer column */
  .answer-box{position:absolute;left:40px;top:75px;width:314px;height:361px;border:1.5px solid var(--ink)}
  .answer-box::after{content:"";position:absolute;left:158px;top:12px;height:336px;border-left:1px dotted var(--ink)}
  .answer-list{list-style:none;position:absolute;top:10px;display:flex;flex-direction:column}
  .answer-list--a{left:8px}
  .answer-list--b{left:183px}
  .answer-list li{width:121px;height:19px;border-bottom:1px solid var(--ink);font-size:7px;padding-top:8px}

  .team-name{position:absolute;font-size:10px;font-weight:700;display:flex;align-items:flex-end;gap:6px}
  .team-name .fill{flex:1;border-bottom:1.2px dotted var(--ink);height:6px}
  .sheet--bingo .team-name{left:386px;top:100px;width:300px}
  .bingo-grid{position:absolute;left:386px;top:134px}

  .instructions{position:absolute;font-size:6.6px;line-height:10.5px;color:#2a2a3a}
  .instructions b{font-weight:700}
  .sheet--bingo .rule{position:absolute;left:40px;top:452px;width:662px;border-top:1px solid var(--ink)}
  .sheet--bingo .instructions{left:40px;top:458px;width:664px}
  .bingo-foot-light{position:absolute;left:0;top:503px;width:736px;height:4px;background:var(--lavender)}
  .bingo-foot-dark{position:absolute;left:0;top:507px;width:736px;height:14px;background:var(--ink)}

  /* Cellraiders sheet */
  .tear-panel{position:absolute;left:0;top:0;width:227px;height:524px;background:var(--ink)}
  .tear-list{list-style:none;position:absolute;left:41px;top:28px}
  .tear-list li{width:150px;height:17px;margin-bottom:2.7px;background:#fff;font-size:7px;padding:5px 0 0 4px;color:var(--ink)}
  .sheet--cells .sheet-title{position:absolute;left:278px;top:22px;font-size:50px;color:var(--ink-deep)}
  .sheet--cells .team-name{left:296px;top:86px;width:296px}
  .hex-grid{position:absolute;left:291px;top:126px}
  .sheet--cells .instructions{left:269px;top:412px;width:436px}
  .sheet--cells .rule{position:absolute;left:269px;top:466px;width:436px;border-top:1px solid var(--ink)}
  .cells-footer{position:absolute;left:265px;top:480px;width:440px;display:flex;align-items:center;color:var(--ink-deep)}
  .cells-footer .contact{font-size:11px;margin-right:12px}
  .cells-footer .brand{margin-left:auto;font-size:14px}
</style>
</head>
<body>

<section class="sheet sheet--bingo" aria-label="Bingo quiz answer sheet">
  <header class="bingo-header">
    <h1 class="sheet-title">BINGO QUIZ</h1>
    <div class="contact">
      <div><svg class="icon" viewBox="0 0 10 10"><circle cx="5" cy="5" r="4.3" fill="none" stroke="#fff"/><path d="M0.7 5h8.6M5 0.7c-2.4 2.6-2.4 6 0 8.6M5 0.7c2.4 2.6 2.4 6 0 8.6" fill="none" stroke="#fff" stroke-width=".8"/></svg>www.marlowtrivet.co.uk</div>
      <div><svg class="icon" viewBox="0 0 10 10"><path d="M2.3 1l1.6 2-0.9 1.1c.6 1.3 1.5 2.2 2.8 2.8l1.1-.9 2 1.6-1 1.4C4.6 8.8 1.2 5.4 1 2z" fill="none" stroke="#fff" stroke-width=".9"/></svg>01632 960481</div>
    </div>
    <div class="brand"><span class="dot"></span>Marlow Trivet</div>
  </header>

  <div class="answer-box">
    <ol class="answer-list answer-list--a">
      <li>1.</li><li>2.</li><li>3.</li><li>4.</li><li>5.</li><li>6.</li><li>7.</li><li>8.</li><li>9.</li>
      <li>10.</li><li>11.</li><li>12.</li><li>13.</li><li>14.</li><li>15.</li><li>16.</li><li>17.</li><li>18.</li>
    </ol>
    <ol class="answer-list answer-list--b">
      <li>19.</li><li>20.</li><li>21.</li><li>22.</li><li>23.</li><li>24.</li><li>25.</li><li>26.</li><li>27.</li>
      <li>28.</li><li>29.</li><li>30.</li><li>31.</li><li>32.</li><li>33.</li><li>34.</li><li>35.</li><li>36.</li>
    </ol>
  </div>

  <div class="team-name">Team Name <span class="fill"></span></div>

  <svg class="bingo-grid" width="301" height="303" viewBox="0 0 301 303">
    <defs>
      <pattern id="bingo-cell" x="9" y="8" width="47.4" height="47.4" patternUnits="userSpaceOnUse">
        <rect x="0" y="0" width="47.4" height="47.4" fill="none" stroke="#3d4599" stroke-width="1"/>
        <circle cx="12.5" cy="12.5" r="8.5" fill="#fff" stroke="#3d4599" stroke-width="1"/>
      </pattern>
    </defs>
    <rect x="0.75" y="0.75" width="299.5" height="301.5" fill="none" stroke="#3d4599" stroke-width="1.5"/>
    <rect x="9" y="8" width="284.4" height="284.4" fill="url(#bingo-cell)" stroke="#3d4599" stroke-width="1"/>
  </svg>

  <div class="rule"></div>
  <p class="instructions"><b>INSTRUCTIONS:</b> The quiz master will call out questions from 1 to 36 – write the number of the question and the answer to it in ANY circle above and copy the answer against the correct number above left. Also write the numbers you use in the corresponding circles bottom left. Once all questions have been read out, tear off the left hand side and hand to the quizmaster. They will now read out the answers in a random order – you need to get a straight line of six correct answers – once you have them shout "HOUSE" and the quizmaster will check your sheet – Good Luck – anyone seen with a mobile phone will have it smashed to pieces with a hammer and will be disqualified!</p>
  <div class="bingo-foot-light"></div>
  <div class="bingo-foot-dark"></div>
</section>

<section class="sheet sheet--cells" aria-label="Cellraiders quiz answer sheet">
  <aside class="tear-panel">
    <ol class="tear-list">
      <li>1.</li><li>1.</li><li>1.</li><li>1.</li><li>1.</li><li>1.</li><li>1.</li><li>1.</li>
      <li>1.</li><li>1.</li><li>1.</li><li>1.</li><li>1.</li><li>1.</li><li>1.</li><li>1.</li>
      <li>1.</li><li>1.</li><li>1.</li><li>1.</li><li>1.</li><li>1.</li><li>1.</li><li>1.</li>
    </ol>
  </aside>

  <h1 class="sheet-title">CELLRAIDER Quiz</h1>
  <div class="team-name">Team Name <span class="fill"></span></div>

  <svg class="hex-grid" width="390" height="272" viewBox="0 0 390 272" font-family="Roboto Condensed, Arial Narrow, sans-serif" font-size="7" fill="#3d4599">
    <defs>
      <g id="hex-cell">
        <polygon points="17,0 51,0 68,29 51,58 17,58 0,29" fill="none" stroke="#3d4599" stroke-width="1"/>
        <text x="20" y="8">No</text>
      </g>
    </defs>
    <use href="#hex-cell" x="0" y="0"/><use href="#hex-cell" x="0" y="60.5"/><use href="#hex-cell" x="0" y="121"/><use href="#hex-cell" x="0" y="181.5"/>
    <use href="#hex-cell" x="52.8" y="29.6"/><use href="#hex-cell" x="52.8" y="90.1"/><use href="#hex-cell" x="52.8" y="150.6"/><use href="#hex-cell" x="52.8" y="211.1"/>
    <use href="#hex-cell" x="105.6" y="0"/><use href="#hex-cell" x="105.6" y="60.5"/><use href="#hex-cell" x="105.6" y="121"/><use href="#hex-cell" x="105.6" y="181.5"/>
    <use href="#hex-cell" x="158.4" y="29.6"/><use href="#hex-cell" x="158.4" y="90.1"/><use href="#hex-cell" x="158.4" y="150.6"/><use href="#hex-cell" x="158.4" y="211.1"/>
    <use href="#hex-cell" x="211.2" y="0"/><use href="#hex-cell" x="211.2" y="60.5"/><use href="#hex-cell" x="211.2" y="121"/><use href="#hex-cell" x="211.2" y="181.5"/>
    <use href="#hex-cell" x="264" y="29.6"/><use href="#hex-cell" x="264" y="90.1"/><use href="#hex-cell" x="264" y="150.6"/><use href="#hex-cell" x="264" y="211.1"/>
    <use href="#hex-cell" x="316.8" y="0"/><use href="#hex-cell" x="316.8" y="60.5"/><use href="#hex-cell" x="316.8" y="121"/><use href="#hex-cell" x="316.8" y="181.5"/>
  </svg>

  <p class="instructions"><b>INSTRUCTIONS:</b> The quiz master will call out questions from 1 to 24 – write the number of the question and the answer to it in ANY hexagon above and copy the answer against the correct number above left. Also write the numbers you use in the corresponding hexagons bottom left. Once all questions have been read out, tear off the left hand side and hand to the quizmaster. They will now read out the answers in a random order – you need to get a straight line of six answers from any of the four squares on the left to any of four squares on the right – once you have them shout "CELLRAIDER" and the quizmaster will check your sheet – Good Luck – anyone seen with a mobile phone will have it smashed to pieces with a hammer and will be disqualified!</p>
  <div class="rule"></div>

  <footer class="cells-footer">
    <span class="contact"><svg class="icon" viewBox="0 0 10 10"><circle cx="5" cy="5" r="4.3" fill="none" stroke="#2c3390"/><path d="M0.7 5h8.6M5 0.7c-2.4 2.6-2.4 6 0 8.6M5 0.7c2.4 2.6 2.4 6 0 8.6" fill="none" stroke="#2c3390" stroke-width=".8"/></svg>www.marlowtrivet.co.uk</span>
    <span class="contact"><svg class="icon" viewBox="0 0 10 10"><path d="M2.3 1l1.6 2-0.9 1.1c.6 1.3 1.5 2.2 2.8 2.8l1.1-.9 2 1.6-1 1.4C4.6 8.8 1.2 5.4 1 2z" fill="none" stroke="#2c3390" stroke-width=".9"/></svg>01632 960481</span>
    <span class="brand"><span class="dot"></span>Marlow Trivet</span>
  </footer>
</section>

</body>
</html>
```